Multi-Faceted Legal and Finanacial Advisory Group Needs Business Card Design

We need a business card design for a newly branded Orlando Florida area advising group consisting of Attorneys, Accountants and Financial Planners. The company is named RT Counsel Group. You will find our initial work on a business card. The information on the business card are merely guideposts and not final product. The logo does not have the be the same as provided since we have not finalized the logo. We would like to stay with a black/white/grey color scheme, but limited use of color is not out of the question.

Target Market(s)

Businesses and their Corporate Representatives

Industry/Entity Type

Business

Contact Information for Business Card

Should have Name, Title, Phone, Cell, Fax, Email and website. Logo should incorporate RT in some fashion however final logo used does not have to be the one on the document provided.

Requirements
Must have
• An RT design on front and back.

```html
<!DOCTYPE html>
<html lang="en">
<head>
<meta charset="utf-8">
<title>RT Counsel Group – Business Card</title>
<link rel="stylesheet" href="https://fonts.googleapis.com/css2?family=Open+Sans:wght@400;600&family=Tinos&display=swap">
<style>
  :root {
    --backdrop: #2b2927;
    --card: #141414;
    --card-back: #0c0c0c;
    --ink: #f2f2f2;
    --ink-soft: #c9c9c9;
    --mark-grey: #5e5e5e;
    --rule: #4a4a4a;
    --frame: #9a9a9a;
  }
  * { margin: 0; padding: 0; box-sizing: border-box; }
  html, body { width: 1200px; height: 844px; overflow: hidden; }
  body {
    background: var(--backdrop);
    font-family: "Open Sans", Arial, sans-serif;
    color: var(--ink);
    position: relative;
  }
  .card {
    position: absolute;
    top: 262px;
    width: 540px;
    height: 320px;
    border-radius: 3px;
    box-shadow: 0 10px 30px rgba(0,0,0,.45);
  }

  /* Front: contact side */
  .card-front {
    left: 40px;
    background: var(--card);
    display: flex;
    align-items: center;
  }
  .brand-block {
    width: 250px;
    display: flex;
    align-items: center;
    justify-content: center;
    gap: 14px;
    padding-left: 20px;
  }
  .brand-square {
    width: 46px;
    height: 46px;
    background: var(--mark-grey);
    flex-shrink: 0;
  }
  .brand-name {
    font-family: "Open Sans", Arial, sans-serif;
    font-weight: 400;
    font-size: 22px;
    line-height: 1.2;
    color: var(--ink);
  }
  .divider {
    width: 1px;
    height: 170px;
    background: var(--rule);
    margin: 0 24px 0 10px;
  }
  .contact { font-size: 13px; line-height: 1.35; color: var(--ink-soft); }
  .contact-name { font-size: 19px; font-weight: 600; color: var(--ink); line-height: 1.2; }
  .contact-title { font-size: 12.5px; margin-bottom: 16px; }
  .contact-lines { margin-bottom: 14px; }

  /* Back: brand side */
  .card-back {
    left: 620px;
    background: var(--card-back);
    display: flex;
    align-items: center;
    justify-content: center;
  }
  .brand-frame {
    width: 440px;
    height: 150px;
    border: 1px solid var(--frame);
    padding: 4px;
  }
  .brand-frame-inner {
    width: 100%;
    height: 100%;
    border: 1px solid var(--rule);
    display: flex;
    align-items: center;
    justify-content: center;
    gap: 14px;
  }
  .back-square {
    width: 58px;
    height: 58px;
    background: var(--mark-grey);
  }
  .back-name {
    font-family: "Tinos", "Times New Roman", serif;
    font-size: 30px;
    color: var(--ink);
    line-height: 1;
  }
  .tagline {
    font-family: "Tinos", "Times New Roman", serif;
    font-size: 9px;
    color: var(--ink-soft);
    margin-top: 6px;
    letter-spacing: .3px;
  }
</style>
</head>
<body>
  <section class="card card-front" aria-label="Business card front">
    <div class="brand-block">
      <div class="brand-square"></div>
      <div class="brand-name">RT Counsel<br>Group</div>
    </div>
    <div class="divider"></div>
    <div class="contact">
      <div class="contact-name">Daniel Reyes</div>
      <div class="contact-title">Managing Director</div>
      <div class="contact-lines">
        T: 407-555 018 244<br>
        E: info@rtcounsel.com<br>
        W: www.rtcounselgroup.com
      </div>
      <div class="contact-address">
        4820, Lakeview Parkway<br>
        Orlando, FL 32801.
      </div>
    </div>
  </section>

  <section class="card card-back" aria-label="Business card back">
    <div class="brand-frame">
      <div class="brand-frame-inner">
        <div class="back-square"></div>
        <div>
          <div class="back-name">RT Counsel Group</div>
          <div class="tagline">Attorneys • Accountants • Financial Planners</div>
        </div>
      </div>
    </div>
  </section>
</body>
</html>
```